Gutschein-Design für Verkauf von Online-Schmuckstücken
Zielgruppe
Wir verkaufen Online Schmuckstücke!
www.feldring-atelier.example
Aufgabenstellung
Wir haben eine schwarze Schachtel erstellt und da drinne wird eine Geschenkgutschein sein:
Es soll sehr schlicht sein und schwarzen Hintergrund haben.
Vorderseite nur unser LOGO.
Rückseite:
Betrag: _________
Gültig Bis: _________
Code: __________
Und unten klein gedruckt steht:
Diese Karte ist gültig nur auf der online shop seite www.feldring-atelier.example und in unserer offizielen Stores. Dieses Karte ist nicht gültig bei rabatierte Produkten und man kann nicht mit dieser karte einen Gutscheinkarte kaufen.
Der Design soll sehr schlicht und dezenz sein.

```html
<!DOCTYPE html>
<html lang="de">
<head>
<meta charset="utf-8">
<title>Gutschein – Feldring Atelier</title>
<link href="https://fonts.googleapis.com/css2?family=Kaushan+Script&family=Open+Sans:wght@300;400;600&family=Oswald:wght@300&display=swap" rel="stylesheet">
<style>
  :root {
    --stage: #1c1a1b;
    --card-dark-a: #423d3f;
    --card-dark-b: #1a1718;
    --card-light: #ffffff;
    --gold: #f7b944;
    --ink: #231f20;
    --line: #f2f2f2;
  }
  html, body {
    margin: 0;
    width: 1200px;
    height: 800px;
    overflow: hidden;
    background: var(--stage);
  }
  .stage {
    width: 1200px;
    height: 800px;
    display: flex;
    flex-direction: column;
    align-items: center;
    justify-content: center;
    gap: 40px;
  }
  .card {
    position: relative;
    width: 640px;
    height: 300px;
    box-sizing: border-box;
    box-shadow: 0 10px 30px rgba(0,0,0,.5);
  }
  .card--back {
    background: linear-gradient(135deg, var(--card-dark-a), var(--card-dark-b) 70%);
    border: 1px solid var(--line);
    color: var(--line);
    font-family: "Open Sans", sans-serif;
  }
  .frame {
    position: absolute;
    left: 106px;
    right: 106px;
    top: 72px;
    height: 150px;
    border: 1.5px solid var(--line);
    border-top: none;
  }
  .frame::before, .frame::after {
    content: "";
    position: absolute;
    top: 0;
    width: 76px;
    border-top: 1.5px solid var(--line);
  }
  .frame::before { left: -1.5px; }
  .frame::after { right: -1.5px; }
  .voucher-title {
    position: absolute;
    top: 22px;
    left: 0;
    right: 0;
    margin: 0;
    text-align: center;
    font-family: "Kaushan Script", cursive;
    font-weight: 400;
    font-size: 60px;
    line-height: 1;
    color: var(--gold);
  }
  .details {
    position: absolute;
    top: 116px;
    left: 0;
    right: 0;
    display: grid;
    grid-template-columns: 1fr 1fr;
    column-gap: 14px;
    row-gap: 4px;
    margin: 0;
    font-weight: 300;
    font-size: 17px;
    line-height: 1.2;
  }
  .details dt { text-align: right; text-transform: uppercase; }
  .details dd { margin: 0; color: var(--gold); }
  .fine-print {
    position: absolute;
    left: 140px;
    right: 140px;
    top: 236px;
    margin: 0;
    text-align: center;
    font-size: 7.6px;
    line-height: 1.3;
  }
  .fine-print .url { color: var(--gold); }
  .card--front {
    background: var(--card-light);
    display: flex;
    flex-direction: column;
    align-items: center;
    justify-content: center;
    gap: 14px;
  }
  .brand {
    display: flex;
    align-items: center;
    gap: 16px;
  }
  .brand-dot {
    width: 52px;
    height: 52px;
    border-radius: 50%;
    background: var(--ink);
  }
  .brand-name {
    font-family: "Open Sans", sans-serif;
    font-weight: 400;
    font-size: 46px;
    color: var(--ink);
    letter-spacing: .5px;
  }
  .brand-url {
    font-family: "Oswald", sans-serif;
    font-weight: 300;
    font-size: 17px;
    letter-spacing: 2.5px;
    color: var(--gold);
  }
</style>
</head>
<body>
<main class="stage">
  <section class="card card--back" aria-label="Gutschein Rückseite">
    <div class="frame"></div>
    <h1 class="voucher-title">Gutschein</h1>
    <dl class="details">
      <dt>Betrag:</dt><dd>100 €</dd>
      <dt>Gültig bis:</dt><dd>01.03.2022</dd>
      <dt>Code:</dt><dd>GSXXX22</dd>
    </dl>
    <p class="fine-print">Diese Karte ist gültig nur auf der Online Shop Seite <span class="url">www.feldring-atelier.example</span> und in unseren offiziellen Stores. Dieses Karte ist nicht gültig bei rabattierten Produkten und man kann nicht mit dieser Karte eine Gutscheinkarte kaufen.</p>
  </section>
  <section class="card card--front" aria-label="Gutschein Vorderseite">
    <div class="brand">
      <span class="brand-dot"></span>
      <span class="brand-name">Feldring Atelier</span>
    </div>
    <span class="brand-url">www.feldring-atelier.example</span>
  </section>
</main>
</body>
</html>
```